Property Management company

We need a design for our company Maplecrest Elder Commons. We are complex of apartments that we manage and operate. We do like the colors green or blue

Industry/Entity Type

Property Management,

Requirements
Must have
• color
Nice to have
• maybe be able to use as a watermark

```html
<!DOCTYPE html>
<html lang="en">
<head>
<meta charset="utf-8">
<title>Maplecrest Elder Commons – Letterhead</title>
<link rel="stylesheet" href="https://fonts.googleapis.com/css2?family=Noto+Serif:wght@400;700&family=Poppins:wght@500;600&display=swap">
<style>
  :root {
    --brand-purple: #6c3893;
    --brand-lilac: #b077b3;
    --ink: #2f2f33;
    --ink-muted: #77767c;
    --paper: #ffffff;
    --watermark: rgba(160, 120, 190, 0.22);
    --signature-tint: #eeeaf2;
  }
  * { box-sizing: border-box; margin: 0; padding: 0; }
  html, body { width: 888px; height: 1200px; overflow: hidden; background: var(--paper); }
  .letterhead {
    position: relative; width: 888px; height: 1200px; background: var(--paper);
    font-family: "Noto Serif", Georgia, serif; color: var(--ink);
  }
  .header-shape { position: absolute; left: 0; top: 0; }
  .brand-name {
    position: absolute; left: 26px; top: 24px; color: var(--paper);
    font-family: "Noto Serif", Georgia, serif; font-weight: 400; line-height: 1;
    text-transform: uppercase;
  }
  .brand-name .line-main { display: block; font-size: 30px; letter-spacing: -0.5px; }
  .brand-name .line-sub { display: block; font-size: 15.5px; margin-top: 5px; letter-spacing: 0.3px; }
  .contact { position: absolute; top: 47px; font-size: 13px; line-height: 24px; }
  .contact b { color: var(--brand-purple); font-weight: 700; }
  .contact-phones { left: 370px; }
  .contact-web { left: 523px; }

  .recipient { position: absolute; left: 26px; top: 204px; }
  .recipient .to-label { font-family: "Poppins", sans-serif; font-size: 12px; font-weight: 500; line-height: 14px; }
  .recipient .name { font-family: "Poppins", sans-serif; font-size: 20px; font-weight: 600; color: var(--brand-purple); line-height: 24px; }
  .recipient .role { font-size: 13px; font-weight: 700; line-height: 20px; margin-top: 1px; }
  .recipient .address { font-size: 13px; color: var(--ink-muted); line-height: 20px; margin-top: 5px; }
  .letter-date { position: absolute; right: 28px; top: 287px; font-size: 12.5px; color: var(--ink-muted); }
  .letter-date b { color: var(--ink); }

  .watermark {
    position: absolute; left: 0; right: 0; top: 600px; text-align: center;
    color: var(--watermark); font-family: "Noto Serif", Georgia, serif; font-weight: 400;
    text-transform: uppercase; line-height: 1; z-index: 0;
  }
  .watermark .line-main { display: block; font-size: 54px; }
  .watermark .line-sub { display: block; font-size: 27px; margin-top: 8px; }

  .letter-body { position: absolute; left: 26px; top: 388px; width: 846px; font-size: 14.2px; line-height: 26px; z-index: 1; }
  .letter-body p { margin-bottom: 26px; }

  .sign-off { position: absolute; left: 26px; top: 898px; width: 204px; }
  .signature-mark { display: block; margin-left: 26px; width: 130px; height: 42px; background: var(--signature-tint); border-radius: 4px; }
  .signature-rule { margin-top: 13px; border-top: 1.5px solid var(--ink); }
  .signature-label {
    margin-top: 10px; text-align: center; font-family: "Poppins", sans-serif; font-weight: 600;
    font-size: 10px; letter-spacing: 6px; color: var(--ink);
  }

  .footer-band { position: absolute; left: 0; top: 1102px; }
  .footer-address {
    position: absolute; left: 168px; width: 552px; top: 1102px; height: 45px; line-height: 45px;
    text-align: center; color: var(--paper); font-size: 13.5px;
  }
</style>
</head>
<body>
<main class="letterhead">
  <svg class="header-shape" width="888" height="120" viewBox="0 0 888 120" aria-hidden="true">
    <path d="M0 0 H888 V11 H346 A70 70 0 0 0 276 81 V114 H0 Z" fill="var(--brand-purple)"/>
  </svg>
  <div class="brand-name">
    <span class="line-main">Maplecrest</span>
    <span class="line-sub">Elder Commons</span>
  </div>
  <div class="contact contact-phones">
    <div><b>P:</b> 555.210.4830</div>
    <div><b>F:</b> 555.210.4831</div>
  </div>
  <div class="contact contact-web">
    <div><b>E:</b> hello@maplecrestcommons.com</div>
    <div><b>W:</b> www.maplecrestcommons.com</div>
  </div>

  <section class="recipient">
    <div class="to-label">To</div>
    <div class="name">Owen Hartley</div>
    <div class="role">CEO, Brightfold Studio</div>
    <div class="address">4820 Linden Park Rd Suite 12<br>Fairbrook, OR 97301</div>
  </section>
  <div class="letter-date"><b>Date:</b> 07-09-2022</div>

  <div class="watermark" aria-hidden="true">
    <span class="line-main">Maplecrest</span>
    <span class="line-sub">Elder Commons</span>
  </div>

  <article class="letter-body">
    <p>Lorem ipsum dolor sit amet, consectetuer adipiscing elit, sed diam nonummy nibh euismod tincidunt ut laoreet dolore magna aliquam erat volutpat. Ut wisi enim ad minim veniam, quis nostrud exerci tation ullamcorper suscipit lobortis nisl ut aliquip ex ea commodo consequat.</p>
    <p>Lorem ipsum dolor sit amet, cons ectetuer adipiscing elit, sed diam nonummy nibh euismod tincidunt ut laoreet dolore magna aliquam erat volutpat. Ut wisi enim ad minim veniam, quis nostrud exerci tation ullamcorper suscipit lobortis nisl ut aliquip ex ea commodo consequat.</p>
    <p>Lorem ipsum dolor sit amet, consectetuer adipiscing elit, sed diam nonummy nibh euismod tincidunt ut laoreet dolore magna aliquam erat volutpat. Ut wisi enim ad minim veniam, quis nostrud exerci tation ullamcorper suscipit lobortis nisl ut aliquip ex ea commodo consequat.</p>
    <p>Lorem ipsum dolor sit amet, consectetuer adipiscing elit, sed diam nonummy nibh euismod tincidunt ut laoreet dolore magna aliquam erat volutpat. Ut wisi enim ad minim veniam, quis nostrud exerci tation ullamcorper suscipit lobortis nisl ut aliquip ex ea commodo consequat. Duis autem vel eum iriure dolor in hendrerit in vulputate velit esse molestie consequat, vel illum dolore eu feugiat nulla facilisis at vero eros et accumsan et iusto odio dignissim qui blandit praesent luptatum zzril delenit augue duis dolore te feugait nulla facilisi.</p>
  </article>

  <section class="sign-off">
    <span class="signature-mark" role="img" aria-label="Handwritten signature"></span>
    <div class="signature-rule"></div>
    <div class="signature-label">SIGNATURE</div>
  </section>

  <svg class="footer-band" width="888" height="45" viewBox="0 0 888 45" aria-hidden="true">
    <polygon points="0,0 158,0 139,45 0,45" fill="var(--brand-purple)"/>
    <polygon points="177,0 729,0 710,45 158,45" fill="var(--brand-lilac)"/>
    <polygon points="748,0 888,0 888,45 729,45" fill="var(--brand-purple)"/>
  </svg>
  <div class="footer-address"><b>Mailing Address:</b> PO Box 520194, Cedar Hollow, TX 75402</div>
</main>
</body>
</html>
```